Re-Design the flow of the Orvane Framework

The orvane framework is a 10 step model that helps teams/organizations become high performing. Attached the model which i created. I love the design as it is but i used a template i don't owe the rights of so i would like to use this platform to see what you can come up with the redesign this flow while keeping the key elements in place. I like the flow, i like the cleanness and i like it to be compact.

Target Market(s)

Organizational change / Leadership/ Consultancy

Industry/Entity Type

Leadership

Requirements
Must have
• Keep as much as possible the flow and feel of the attached
Nice to have
• -Maybe some twist in how the different parts connect (not a must)
Should not have
• Less or more steps than added in the attached file

```html
<!DOCTYPE html>
<html lang="en">
<head>
<meta charset="utf-8">
<title>Orvane Framework – Capability Flow</title>
<link rel="stylesheet" href="https://fonts.googleapis.com/css2?family=Montserrat:wght@600;700&display=swap">
<style>
  :root {
    --bg: #fdfdfd;
    --lime-light: #c1ef4f;
    --lime: #d0e021;
    --orange: #e06a20;
    --cyan: #00d9fb;
    --sky: #00bfff;
    --crimson: #c72c48;
    --green: #57e900;
    --green-deep: #1fd200;
    --pink: #cc66a6;
    --plum: #b14086;
    --label-red: #c8283f;
    --label-white: #ffffff;
    --hub-text: #222222;
    --hub-fill: #ffffff;
  }
  html, body {
    margin: 0;
    padding: 0;
    width: 1200px;
    height: 1200px;
    overflow: hidden;
    background: var(--bg);
  }
  .framework {
    display: block;
    width: 1200px;
    height: 1200px;
  }
  .wheel {
    filter: drop-shadow(14px 16px 14px rgba(0, 0, 0, 0.28));
  }
  .hub {
    fill: var(--hub-fill);
    filter: drop-shadow(6px 8px 6px rgba(0, 0, 0, 0.25));
  }
  .step-label {
    font-family: "Montserrat", Arial, sans-serif;
    font-weight: 600;
    font-size: 21px;
    letter-spacing: 0.3px;
  }
  .step-label--red { fill: var(--label-red); }
  .step-label--white { fill: var(--label-white); }
  .hub-label {
    font-family: "Montserrat", Arial, sans-serif;
    font-weight: 600;
    font-size: 26px;
    fill: var(--hub-text);
    text-anchor: middle;
  }
  .seg-lime-light { fill: var(--lime-light); }
  .seg-lime { fill: var(--lime); }
  .seg-orange { fill: var(--orange); }
  .seg-cyan { fill: var(--cyan); }
  .seg-sky { fill: var(--sky); }
  .seg-crimson { fill: var(--crimson); }
  .seg-green { fill: var(--green); }
  .seg-green-deep { fill: var(--green-deep); }
  .seg-pink { fill: var(--pink); }
  .seg-plum { fill: var(--plum); }
</style>
</head>
<body>
<svg class="framework" viewBox="0 0 1920 1920" xmlns="http://www.w3.org/2000/svg" aria-label="Orvane Framework: ten capabilities across two connected wheels">
  <g class="wheel">
    <!-- foundation wheel, lower half -->
    <path class="seg-sky" d="M688 910 L1060 910 A372 372 0 0 1 617 1275.2 Z"/>
    <path class="seg-cyan" d="M688 910 L617 1275.2 A372 372 0 0 1 316 910 Z"/>

    <!-- excellence wheel -->
    <path class="seg-crimson" d="M1198 910 L826 910 A372 372 0 0 1 1289.9 549.5 Z"/>
    <path class="seg-green" d="M1198 910 L1289.9 549.5 A372 372 0 0 1 1564.8 847.9 Z"/>
    <path class="seg-green-deep" d="M1198 910 L1564.8 847.9 A372 372 0 0 1 1406 1218.4 Z"/>
    <path class="seg-pink" d="M1198 910 L1406 1218.4 A372 372 0 0 1 1032.1 1242.9 Z"/>
    <path class="seg-plum" d="M1198 910 L1032.1 1242.9 A372 372 0 0 1 826 910 Z"/>

    <!-- foundation wheel, upper half -->
    <path class="seg-lime-light" d="M688 910 L316 910 A372 372 0 0 1 562.6 559.9 Z"/>
    <path class="seg-lime" d="M688 910 L562.6 559.9 A372 372 0 0 1 970.9 668.4 Z"/>
    <path class="seg-orange" d="M688 910 L970.9 668.4 A372 372 0 0 1 1060 910 Z"/>
  </g>

  <circle class="hub" cx="688" cy="910" r="137"/>
  <circle class="hub" cx="1198" cy="910" r="137"/>

  <text class="hub-label">
    <tspan x="684" y="888">Capabilities</tspan>
    <tspan x="684" y="915">driving a solid</tspan>
    <tspan x="684" y="942">foundation</tspan>
  </text>
  <text class="hub-label">
    <tspan x="1198" y="888">Capabilities</tspan>
    <tspan x="1200" y="915">maximizing</tspan>
    <tspan x="1200" y="942">excellence</tspan>
  </text>

  <text class="step-label step-label--red">
    <tspan x="607" y="623">Tap into peoples</tspan>
    <tspan x="607" y="646">Purpose and</tspan>
    <tspan x="607" y="669">Passion (intrinsic</tspan>
    <tspan x="607" y="692">motivation)</tspan>
  </text>
  <text class="step-label step-label--red">
    <tspan x="398" y="766">Cultivate</tspan>
    <tspan x="398" y="789">Psychological</tspan>
    <tspan x="398" y="812">Safety and</tspan>
    <tspan x="398" y="835">Ownership</tspan>
  </text>
  <text class="step-label step-label--white">
    <tspan x="848" y="755">Unlock culture</tspan>
    <tspan x="848" y="778">of personal</tspan>
    <tspan x="848" y="801">growth &amp;</tspan>
    <tspan x="848" y="824">development</tspan>
  </text>
  <text class="step-label step-label--red">
    <tspan x="419" y="1011">Develop a</tspan>
    <tspan x="419" y="1034">Master plan</tspan>
    <tspan x="419" y="1057">(strategy)</tspan>
  </text>
  <text class="step-label step-label--red">
    <tspan x="672" y="1128">Identify</tspan>
    <tspan x="672" y="1151">Purpose</tspan>
    <tspan x="672" y="1174">Activators</tspan>
    <tspan x="672" y="1197">(Vision)</tspan>
  </text>
  <text class="step-label step-label--white">
    <tspan x="909" y="997">Prioritize</tspan>
    <tspan x="909" y="1020">Feedback &amp;</tspan>
    <tspan x="909" y="1043">Transparency</tspan>
  </text>
  <text class="step-label step-label--white">
    <tspan x="1081" y="643">Discover your</tspan>
    <tspan x="1081" y="666">purpose. Why</tspan>
    <tspan x="1081" y="689">Do you exist?</tspan>
  </text>
  <text class="step-label step-label--white">
    <tspan x="1348" y="743">Monitor</tspan>
    <tspan x="1348" y="766">engagement</tspan>
    <tspan x="1348" y="789">Real-time</tspan>
  </text>
  <text class="step-label step-label--white">
    <tspan x="1324" y="1020">Put excellent (team)</tspan>
    <tspan x="1324" y="1043">performance in</tspan>
    <tspan x="1324" y="1066">the spotlight</tspan>
  </text>
  <text class="step-label step-label--white">
    <tspan x="1124" y="1141">Empower the</tspan>
    <tspan x="1124" y="1164">community from</tspan>
    <tspan x="1124" y="1187">bottom-up</tspan>
  </text>
</svg>
</body>
</html>
```